Business Card and Word .doc header and footer required

I need a business card designed for my cybersecurity consulting company. Also required, is a header and footer to be ued for my word documents.
Attached is the Logo design, font and rgb used.

Industry/Entity Type

Cyber Security Consulting

Contact Information for Business Card

Name, Phone, email, website

Colors
0054AA
0677BA
7BADD7
CADEEF
E8F1F8

Requirements
Must have
• Sleek, modern

```html
<!DOCTYPE html>
<html lang="en">
<head>
<meta charset="utf-8">
<title>Hartwell Row Consulting – Letterhead</title>
<link href="https://fonts.googleapis.com/css2?family=Open+Sans:wght@400;600&family=Lato:wght@400;700&display=swap" rel="stylesheet">
<style>
  :root {
    --backdrop: #dcdfe6;
    --paper: #ffffff;
    --brand-blue: #0e78a6;
    --brand-navy: #1b1f3a;
    --ink: #555a60;
    --ink-strong: #1c1f26;
    --rule: #9fc9de;
  }
  * { margin: 0; padding: 0; box-sizing: border-box; }
  html, body {
    width: 1062px; height: 1200px; overflow: hidden;
    background: var(--backdrop);
    font-family: "Open Sans", sans-serif;
  }
  .letterhead {
    position: absolute; left: 234px; top: 260px;
    width: 594px; height: 767px;
    background: var(--paper);
  }
  .edge-bar { position: absolute; left: 0; width: 8px; }
  .edge-bar--top { top: 0; height: 319px; background: var(--brand-blue); }
  .edge-bar--bottom { top: 323px; bottom: 0; background: var(--brand-navy); }

  .brand {
    position: absolute; left: 381px; top: 26px; width: 180px;
    display: flex; flex-direction: column; align-items: center;
  }
  .brand__mark {
    width: 48px; height: 48px; border-radius: 50%;
    border: 5px solid var(--brand-blue);
  }
  .brand__name {
    margin-top: 10px;
    font-weight: 600; font-size: 15px; line-height: 18px;
    letter-spacing: 0.4px; text-align: center; text-transform: uppercase;
    color: var(--brand-navy); white-space: nowrap;
  }
  .brand__name small {
    display: block; font-size: 7.5px; line-height: 10px; letter-spacing: 2.4px;
  }

  .letter { position: absolute; left: 56px; width: 480px; color: var(--ink); font-size: 9.8px; }
  .letter p { line-height: 11.6px; }
  .issue-date { top: 152px; }
  .recipient { top: 174px; }
  .salutation { top: 241px; }
  .body { top: 272px; font-size: 9.5px; }
  .body p { line-height: 17.2px; text-align: justify; hyphens: auto; margin-bottom: 17.2px; }
  .closing { top: 533px; }
  .signature {
    display: block; width: 136px; height: 16px; margin: 12px 0 8px;
    background: linear-gradient(90deg, #e4e5e8, #f3f3f5);
    border-radius: 2px;
  }
  .letter .signer-name { font-size: 12px; font-weight: 600; color: var(--ink); line-height: 16px; }
  .letter .signer-title { margin-top: 3px; }

  .footer {
    position: absolute; left: 0; right: 0; top: 718px;
    font-family: "Lato", sans-serif; color: var(--ink-strong);
    text-align: center; font-size: 11.2px;
  }
  .footer__address { line-height: 14px; }
  .footer__rule { width: 368px; height: 1px; background: var(--rule); margin: 2px auto 4px 114px; }
  .footer__contact { line-height: 14px; }
  .footer__contact b { font-weight: 700; color: var(--brand-navy); }
</style>
</head>
<body>
  <main class="letterhead">
    <div class="edge-bar edge-bar--top"></div>
    <div class="edge-bar edge-bar--bottom"></div>

    <header class="brand">
      <div class="brand__mark"></div>
      <div class="brand__name">Hartwell Row<small>Consulting</small></div>
    </header>

    <p class="letter issue-date">Issuing Date: May 5, 2018</p>
    <div class="letter recipient">
      <p>Name Of Employee Mr. XYZABC</p>
      <p>Address of Employee</p>
      <p>Address Line 2 etc..</p>
    </div>
    <p class="letter salutation">Dear Mr.XYZABC</p>

    <div class="letter body">
      <p>Lorem Ipsum has been the industry's standard dummy text ever since the 1500s, when an unknown printer took a galley of type and scrambled it to make a type specimen book. It has survived not only five centuries, but also the leap into electronic typesetting, remaining essentially unchanged. It was popularised in the 1960s with the release of Letraset sheets containing Lorem Ipsum passages, and more recently with desktop publishing software like Aldus PageMaker including versions of Lorem Ipsum.</p>
      <p>Lorem Ipsum is simply dummy text of the printing and typesetting industry. Lorem Ipsum has been the industry's standard dummy text ever since the 1500s, when an unknown printer took a galley of type and scrambled it to make a type specimen book.</p>
      <p>It has survived not only five centuries, but also the leap into electronic typesetting, remaining essentially unchanged. It was popularised in the 1960s with the release of Letraset sheets containing Lorem IpsumIpsum passages.</p>
    </div>

    <div class="letter closing">
      <p>Yours Sincerely</p>
      <span class="signature" role="img" aria-label="Handwritten signature of Marcus Ellery"></span>
      <p class="signer-name">Marcus Ellery</p>
      <p class="signer-title">Managing Director</p>
    </div>

    <footer class="footer">
      <p class="footer__address">421, Address line here Country Name, 45452</p>
      <div class="footer__rule"></div>
      <p class="footer__contact"><b>P:</b> 021-555 018 342 &nbsp;|&nbsp; <b>E:</b> hello@hartwellrow.com &nbsp;| <b>W:</b> www.hartwellrow.com</p>
    </footer>
  </main>
</body>
</html>
```